Regenerative Medicine Brochure

I want a clean modern bi-fold or tri-fold brochure. We offer non-surgical joint repair for knees, shoulders, and hips. We have many services available including regenerative medicine including stem cell allograft, palatelet rich plasma, prolotherapy, triggerpoint injection, chiropractic and rehab therapies. We are a modern multidisciplinary clinic in coastal California. My logo is already complete and is a vibrant green color. I prefer lots of white space with some areas for service description and what conditions may benefit from the services. Design should convey modern treatments, upscale office and practice, and our target audience is older adults who want to maintain an active pain-free lifestyle.

Target Market(s)

Sports injuries, athletes, seniors who are active, knee pain, shoulder pain, arthritis.

Industry/Entity Type

Alternative Medicine

Font styles to use
Serif

Colors
9bcb3c

Requirements
Must have
• Small white space where we can write date, time, location of next event/class. Colors in brochure to coordinate with logo colors provided.

```html
<!DOCTYPE html>
<html lang="en">
<head>
<meta charset="utf-8">
<title>Regenerative Medicine Brochure</title>
<link rel="stylesheet" href="https://fonts.googleapis.com/css2?family=Poppins:ital,wght@0,400;0,600;0,700;1,300&family=Didact+Gothic&display=swap">
<style>
  :root {
    --green: #7ed957;
    --ink: #1e1e1e;
    --paper: #f9f9f9;
    --card: #ffffff;
    --rule: #d9d9d9;
    --photo-light: #eef4f8;
    --photo-mid: #cfdfe9;
  }
  * { margin: 0; padding: 0; box-sizing: border-box; }
  html, body { width: 1200px; height: 927px; overflow: hidden; background: var(--paper); }
  .brochure { position: relative; width: 1200px; height: 927px; background: var(--paper); }

  .heading {
    position: absolute;
    color: var(--green);
    font-family: "Poppins", sans-serif;
    font-weight: 700;
    font-size: 29px;
    line-height: 36px;
    text-align: center;
    text-transform: uppercase;
  }
  .body-copy {
    position: absolute;
    color: var(--ink);
    font-family: "Didact Gothic", sans-serif;
    font-size: 12.3px;
    line-height: 20.5px;
    text-align: center;
  }

  .info-column .heading { left: 0; width: 403px; }
  .info-column .body-copy { left: 46px; width: 312px; }

  .hero-photo {
    position: absolute; left: 405px; top: 0; width: 396px; height: 528px;
    background: linear-gradient(135deg, var(--photo-light) 0%, #f6f9fb 45%, var(--photo-mid) 100%);
  }
  .accent-band { position: absolute; left: 0; top: 528px; width: 801px; height: 22px; background: var(--green); }

  .tagline {
    position: absolute; left: 420px; top: 665px; width: 364px;
    color: var(--green);
    font-family: "Poppins", sans-serif; font-weight: 300; font-style: italic;
    font-size: 21px; line-height: 43px; letter-spacing: 4px;
    text-align: center; text-transform: uppercase;
  }

  .services-panel .heading { left: 801px; width: 399px; font-size: 43px; line-height: 50px; top: 240px; }
  .service-title {
    position: absolute; left: 801px; width: 399px;
    color: var(--green);
    font-family: "Poppins", sans-serif; font-weight: 600;
    font-size: 15px; letter-spacing: 2.5px; text-align: center; text-transform: uppercase;
  }
  .services-panel .body-copy { left: 852px; width: 296px; }

  .event-card {
    position: absolute; left: 862px; top: 740px; width: 276px; height: 132px;
    background: var(--card);
    border: 2px solid var(--green);
    padding: 14px 20px 0;
  }
  .event-label {
    color: var(--green);
    font-family: "Poppins", sans-serif; font-weight: 600;
    font-size: 13px; letter-spacing: 2.5px; text-align: center; text-transform: uppercase;
    margin-bottom: 8px;
  }
  .event-field {
    display: flex; align-items: flex-end; gap: 8px;
    height: 26px;
    font-family: "Didact Gothic", sans-serif; font-size: 12.3px; color: var(--ink);
  }
  .event-field span { width: 62px; }
  .event-field i { flex: 1; border-bottom: 1px solid var(--rule); height: 16px; }
</style>
</head>
<body>
<main class="brochure">
  <section class="info-column">
    <h2 class="heading" style="top:30px">What is regenerative<br>medicine?</h2>
    <p class="body-copy" style="top:132px">Regenerative medicine uses your body's own healing power to repair worn or injured joints without surgery. Our team treats knees, shoulders and hips so you can keep walking, golfing and playing with less pain and a faster return to the things you enjoy.</p>

    <h2 class="heading" style="top:278px">How does regenerative<br>medicine work?</h2>
    <p class="body-copy" style="top:377px">Carefully guided injections deliver growth factors and healing cells right where tissue is damaged. They calm inflammation, support new cartilage and tendon growth, and strengthen loose ligaments, while chiropractic and rehab care restore motion and balance.</p>

    <h2 class="heading" style="top:574px">What can I expect<br>from regenerative<br>medicine treatments?</h2>
    <p class="body-copy" style="top:713px">Most visits take under an hour in our calm, modern office, with little downtime. Patients with arthritis, sports injuries, torn tendons or chronic knee and shoulder pain often notice steady gains over several weeks as the joint heals.</p>
  </section>

  <div class="hero-photo" role="img" aria-label="Photo of a smiling doctor in a white coat with a stethoscope, a nurse standing behind him in a bright clinic"></div>
  <div class="accent-band"></div>

  <p class="tagline">Our new clinic is here<br>to help the residents<br>of our neighborhood.</p>

  <section class="services-panel">
    <h2 class="heading">Services</h2>

    <h3 class="service-title" style="top:319px">Stem cell &amp; PRP</h3>
    <p class="body-copy" style="top:353px">Stem cell allograft and platelet rich plasma injections help rebuild damaged cartilage, tendons and ligaments in the knee, shoulder and hip.</p>

    <h3 class="service-title" style="top:456px">Prolotherapy</h3>
    <p class="body-copy" style="top:490px">Prolotherapy firms up loose, weak ligaments, and trigger point injections ease tight, knotted muscles for lasting relief from joint pain.</p>

    <h3 class="service-title" style="top:593px">Chiropractic &amp; rehab</h3>
    <p class="body-copy" style="top:627px">Chiropractic adjustments and guided rehab therapy restore strength, balance and motion so you stay active and pain free.</p>

    <aside class="event-card">
      <p class="event-label">Next event</p>
      <div class="event-field"><span>Date</span><i></i></div>
      <div class="event-field"><span>Time</span><i></i></div>
      <div class="event-field"><span>Location</span><i></i></div>
    </aside>
  </section>
</main>
</body>
</html>
```